6 Sizes Set - Static Banners

We have an html template for our newsletter which include graphic elements and we need images to populate these fixed Grey spaces.

Attachment 1: PLEASE READ FULL Graphic Brief is the complete brief describing all fine details.

Attachment 2: layout, shows the example of template

Attachment 3: We need the 6 image sizes (i.e. different fonts, backgrounds, colors, casino icons) – attached Styles Folder for an idea of the variety. These are just a few examples.

Target Market(s)

global

Industry/Entity Type

Casino

Requirements
Must have
• Refer to attach Full brief, for complete explanation
Nice to have
• Second Place: refer to Screenshot
Perfect example of what to submit

```html
<!DOCTYPE html>
<html lang="en">
<head>
<meta charset="utf-8">
<title>Casino Newsletter Banner Set</title>
<link href="https://fonts.googleapis.com/css2?family=Russo+One&family=Audiowide&display=swap" rel="stylesheet">
<style>
:root{
  --page:#ffffff;
  --edge:#222222;
  --vip-bg:#575757;
  --vip-red:#e0262b;
  --spin-dark:#233424;
  --spin-lime:#9ccc3c;
  --spin-orange:#f7a000;
  --cash-purple:#7b3c9f;
  --cash-purple-deep:#56236f;
  --cash-pink:#ff1fc6;
  --cash-blue:#0f4aa0;
  --chip-tone-a:#9a9a9a;
  --chip-tone-b:#3a3a3a;
  --wheel-tone-a:#8a3a1c;
  --wheel-tone-b:#3a1a10;
  --stack-tone-a:#d8475a;
  --stack-tone-b:#e6a83a;
  --money-tone-a:#e2e5da;
  --money-tone-b:#b9a58e;
  --white:#ffffff;
}
*{box-sizing:border-box;margin:0;padding:0}
html,body{width:1200px;height:800px;overflow:hidden;background:var(--page)}
.canvas{position:relative;width:1200px;height:800px}
.banner{position:absolute;overflow:hidden;border:1px solid var(--edge);display:flex;align-items:center;justify-content:center;text-align:center}
.banner--notch-bottom::after,.banner--notch-top::after{content:"";position:absolute;left:50%;width:0;height:0;transform:translateX(-50%);border-left:9px solid transparent;border-right:9px solid transparent;z-index:5}
.banner--notch-bottom::after{bottom:-1px;border-bottom:9px solid var(--white)}
.banner--notch-top::after{top:-1px;border-top:9px solid var(--white)}

.theme-vip{background:var(--vip-bg)}
.theme-spins{background:linear-gradient(90deg,var(--spin-dark),var(--spin-lime))}
.theme-spins.tall{background:linear-gradient(180deg,#4d7a32,var(--spin-dark))}
.theme-cash{background:radial-gradient(circle at 50% 40%,var(--cash-purple),var(--cash-purple-deep))}

.headline{position:relative;z-index:3;font-family:"Russo One",sans-serif;line-height:1;text-transform:uppercase;white-space:nowrap}
.headline--vip{color:var(--vip-red);text-shadow:-2px -2px 0 var(--white),2px -2px 0 var(--white),-2px 2px 0 var(--white),2px 2px 0 var(--white),3px 4px 4px rgba(0,0,0,.7)}
.headline--spins{color:var(--spin-orange);text-shadow:-2px -2px 0 #000,2px -2px 0 #000,-2px 2px 0 #000,2px 2px 0 #000,3px 4px 4px rgba(0,0,0,.6)}
.headline--pink{color:var(--cash-pink);text-shadow:-2px -2px 0 var(--white),2px -2px 0 var(--white),-2px 2px 0 var(--white),2px 2px 0 var(--white),3px 4px 4px rgba(0,0,0,.6)}
.headline--blue{font-family:"Audiowide",sans-serif;color:var(--cash-blue);text-shadow:-2px -2px 0 var(--white),2px -2px 0 var(--white),-2px 2px 0 var(--white),2px 2px 0 var(--white),3px 4px 4px rgba(0,0,0,.6)}
.small .headline{text-shadow:-1px -1px 0 var(--white),1px -1px 0 var(--white),-1px 1px 0 var(--white),1px 1px 0 var(--white)}
.small .headline--spins{text-shadow:-1px -1px 0 #000,1px -1px 0 #000,-1px 1px 0 #000,1px 1px 0 #000}

.art{position:absolute;z-index:1;border-radius:6px}
.art--chip{background:radial-gradient(closest-side,var(--chip-tone-a),var(--chip-tone-b) 90%,transparent)}
.art--wheel{background:radial-gradient(closest-side,var(--wheel-tone-a),var(--wheel-tone-b) 85%,transparent)}
.art--chips{background:linear-gradient(90deg,var(--stack-tone-a),var(--stack-tone-b))}
.art--money{background:linear-gradient(135deg,var(--money-tone-a),var(--money-tone-b))}
</style>
</head>
<body>
<main class="canvas">

  <div class="banner small theme-vip" style="left:60px;top:42px;width:45px;height:45px">
    <div class="art art--chip" role="img" aria-label="Poker chip illustration" style="width:24px;height:24px;left:10px;top:2px"></div>
    <span class="headline headline--vip" style="font-size:9px;margin-top:16px">VIP<br>Rewards</span>
  </div>
  <div class="banner small theme-spins tall" style="left:170px;top:42px;width:45px;height:45px">
    <div class="art art--wheel" role="img" aria-label="Roulette wheel illustration" style="width:45px;height:22px;left:0;bottom:0"></div>
    <span class="headline headline--spins" style="font-size:7px;margin-top:-14px">Free Spins<br>Giveaway</span>
  </div>
  <div class="banner small theme-cash" style="left:271px;top:42px;width:45px;height:45px">
    <div class="art art--chips" role="img" aria-label="Casino chip stacks and cash" style="width:45px;height:14px;left:0;bottom:0"></div>
    <span class="headline headline--pink" style="font-size:9px;margin-top:-12px">Best<br><span style="font-size:6px">Cashbacks</span></span>
  </div>
  <div class="banner small theme-cash" style="left:390px;top:42px;width:45px;height:45px;background:var(--white)">
    <div class="art art--money" role="img" aria-label="Chips and banknotes" style="width:45px;height:18px;left:0;bottom:0"></div>
    <span class="headline headline--blue" style="font-size:10px;margin-top:-14px">Best<br><span style="font-size:6px">Cashbacks</span></span>
  </div>

  <div class="banner small theme-vip" style="left:47px;top:110px;width:70px;height:80px">
    <div class="art art--chip" role="img" aria-label="Poker chip illustration" style="width:70px;height:40px;left:0;top:0"></div>
    <span class="headline headline--vip" style="font-size:17px;margin-top:36px">VIP<br><span style="font-size:10px">Rewards</span></span>
  </div>
  <div class="banner small theme-spins tall" style="left:157px;top:110px;width:70px;height:80px">
    <div class="art art--wheel" role="img" aria-label="Roulette wheel illustration" style="width:70px;height:46px;left:0;bottom:0"></div>
    <span class="headline headline--spins" style="font-size:10px;margin-top:-38px">Free Spins<br>Giveaway</span>
  </div>
  <div class="banner small theme-cash" style="left:259px;top:110px;width:70px;height:80px">
    <div class="art art--chips" role="img" aria-label="Casino chip stacks" style="width:30px;height:38px;left:0;bottom:0"></div>
    <div class="art art--money" role="img" aria-label="Hand holding banknotes" style="width:38px;height:36px;right:0;bottom:0"></div>
    <span class="headline headline--pink" style="font-size:17px;margin-top:-28px">Best<br><span style="font-size:10px">Cashbacks</span></span>
  </div>
  <div class="banner small theme-cash" style="left:378px;top:110px;width:70px;height:80px">
    <div class="art art--money" role="img" aria-label="Chips and banknotes" style="width:70px;height:44px;left:0;bottom:0"></div>
    <span class="headline headline--blue" style="font-size:17px;margin-top:-34px">Best<br><span style="font-size:8px">Cashbacks</span></span>
  </div>

  <div class="banner banner--notch-top theme-vip" style="left:545px;top:42px;width:210px;height:60px">
    <div class="art art--chip" role="img" aria-label="Poker chip illustration" style="width:60px;height:58px;left:0;top:0"></div>
    <div class="art art--chip" role="img" aria-label="Poker chip illustration" style="width:60px;height:58px;right:0;top:0"></div>
    <span class="headline headline--vip" style="font-size:21px">VIP Rewards</span>
  </div>
  <div class="banner banner--notch-top theme-spins" style="left:545px;top:130px;width:210px;height:60px">
    <div class="art art--wheel" role="img" aria-label="Roulette wheel illustration" style="width:92px;height:58px;left:0;top:0"></div>
    <span class="headline headline--spins" style="position:absolute;left:96px;top:13px;font-size:16px">Free Spins<br>Giveaway</span>
  </div>
  <div class="banner banner--notch-top theme-cash" style="left:864px;top:45px;width:210px;height:60px">
    <div class="art art--chips" role="img" aria-label="Casino chip stacks" style="width:34px;height:30px;left:0;bottom:0"></div>
    <div class="art art--money" role="img" aria-label="Hand holding banknotes" style="width:40px;height:58px;right:0;bottom:0"></div>
    <span class="headline headline--pink" style="font-size:16px">Best Cashbacks</span>
  </div>
  <div class="banner banner--notch-top theme-cash" style="left:864px;top:130px;width:210px;height:60px">
    <div class="art art--chips" role="img" aria-label="Casino chip stacks" style="width:60px;height:58px;left:0;bottom:0"></div>
    <div class="art art--money" role="img" aria-label="Hand holding banknotes" style="width:80px;height:58px;right:0;bottom:0"></div>
    <span class="headline headline--blue" style="font-size:17px">Best Cashbacks</span>
  </div>

  <div class="banner banner--notch-bottom theme-vip" style="left:144px;top:219px;width:200px;height:130px">
    <div class="art art--chip" role="img" aria-label="Poker chip illustration" style="width:58px;height:58px;left:2px;top:2px"></div>
    <div class="art art--chip" role="img" aria-label="Poker chip illustration" style="width:58px;height:58px;right:2px;top:2px"></div>
    <span class="headline headline--vip" style="font-size:38px;margin-top:6px">VIP<br><span style="font-size:32px">Rewards</span></span>
  </div>
  <div class="banner banner--notch-bottom theme-spins tall" style="left:144px;top:363px;width:200px;height:130px">
    <div class="art art--wheel" role="img" aria-label="Roulette wheel illustration" style="width:180px;height:50px;left:10px;bottom:0"></div>
    <span class="headline headline--spins" style="font-size:26px;margin-top:-40px;line-height:1.25">Free Spins<br>Giveaway</span>
  </div>
  <div class="banner banner--notch-bottom theme-cash" style="left:144px;top:508px;width:200px;height:130px">
    <div class="art art--chips" role="img" aria-label="Casino chip stacks" style="width:72px;height:50px;left:0;bottom:0"></div>
    <div class="art art--money" role="img" aria-label="Hand holding banknotes" style="width:68px;height:56px;right:0;bottom:0"></div>
    <span class="headline headline--pink" style="font-size:26px;margin-top:-40px;line-height:1.1">Best<br>Cashbacks</span>
  </div>
  <div class="banner banner--notch-bottom theme-cash" style="left:144px;top:652px;width:200px;height:130px">
    <div class="art art--chips" role="img" aria-label="Casino chip stacks" style="width:90px;height:66px;left:0;bottom:0"></div>
    <div class="art art--money" role="img" aria-label="Hand holding banknotes" style="width:100px;height:86px;right:0;bottom:0"></div>
    <span class="headline headline--blue" style="font-size:38px;margin-top:-50px;line-height:.95">Best<br><span style="font-size:19px">Cashbacks</span></span>
  </div>

  <div class="banner banner--notch-bottom theme-vip" style="left:463px;top:239px;width:640px;height:90px">
    <div class="art art--chip" role="img" aria-label="Poker chip illustration" style="width:84px;height:84px;left:16px;top:2px"></div>
    <div class="art art--chip" role="img" aria-label="Poker chip illustration" style="width:84px;height:84px;right:20px;top:2px"></div>
    <span class="headline headline--vip" style="font-size:48px">VIP Rewards</span>
  </div>
  <div class="banner banner--notch-bottom theme-spins" style="left:463px;top:383px;width:640px;height:90px">
    <div class="art art--wheel" role="img" aria-label="Roulette wheel illustration" style="width:170px;height:88px;left:0;top:0"></div>
    <span class="headline headline--spins" style="position:absolute;left:174px;top:25px;font-size:35px">Free Spins Giveaway</span>
  </div>
  <div class="banner banner--notch-bottom theme-cash" style="left:463px;top:528px;width:640px;height:90px">
    <div class="art art--chips" role="img" aria-label="Casino chip stacks" style="width:130px;height:88px;left:0;bottom:0"></div>
    <div class="art art--money" role="img" aria-label="Hand holding banknotes" style="width:135px;height:88px;right:0;bottom:0"></div>
    <span class="headline headline--pink" style="font-size:36px">Best Cashbacks</span>
  </div>
  <div class="banner banner--notch-bottom theme-cash" style="left:463px;top:672px;width:640px;height:90px">
    <div class="art art--chips" role="img" aria-label="Casino chip stacks" style="width:130px;height:88px;left:0;bottom:0"></div>
    <div class="art art--money" role="img" aria-label="Hand holding banknotes" style="width:135px;height:88px;right:0;bottom:0"></div>
    <span class="headline headline--blue" style="font-size:40px">Best Cashbacks</span>
  </div>

</main>
</body>
</html>
```